Real Estate Agent Service Brochure

I need a trifold brochure to showcase my real estate services. I am a veteran Real Estate Broker specializing in marketing properties for sale and for top dollar. I would like to see designs that use colors from my logo (attached) and I would like to showcase some before and after photos of staging jobs I have done to homes to get them ready for the market. This brochure is specific to home sellers. You are happy to go check out my website for inspiration www.lomavertpa.com but keep the copy as I have written it. The the final design should communicate experienced professional who uses current technologies and strategies to market properties for the highest value.

Target Market(s)

Homeowners wanting to sell their homes

Industry/Entity Type

Real Estate Agent

Font styles to use
Serif

Requirements
Must have
• My, logo, personal photo, title and contact information as listed:
• Marta Venholt
• Owner Broker
• Stager Re-Designer
• 860-912-7048
• BRAVE Realty LLC
• LOMAVERTPA.com
• Marta@LOMAVERTPA.com
• The colors used should be those in my logo.
• Brochure should be able to fit in standard envelope for mailing.
Nice to have
• I think I would like my personal photo and contact information on the front panel.
Should not have
• Bright colors.

```html
<!DOCTYPE html>
<html lang="en">
<head>
<meta charset="utf-8">
<title>BRAVE Realty LLC – Seller Brochure</title>
<link href="https://fonts.googleapis.com/css2?family=Open+Sans:wght@400;600;700&family=Montserrat:wght@600;700;800&display=swap" rel="stylesheet">
<style>
:root{
  --blue:#1f5287;
  --blue-dark:#173f69;
  --charcoal:#3b3d40;
  --grey:#6b6e72;
  --light:#eceded;
  --paper:#ffffff;
  --line:#d3d5d8;
}
*{box-sizing:border-box;margin:0;padding:0}
html,body{width:786px;height:1200px;overflow:hidden;background:#f4f4f4}
body{position:relative;font-family:"Open Sans",Arial,sans-serif;color:var(--grey)}
.spread{position:absolute;left:0;width:786px;background:var(--paper);overflow:hidden}
.spread.outer{top:0;height:600px}
.spread.inner{top:612px;height:588px}
.panel{position:absolute;top:0;height:100%;width:262px}
.p1{left:0}.p2{left:262px}.p3{left:524px}
.heading{font-family:Montserrat,Arial,sans-serif;font-weight:700;text-transform:uppercase;color:var(--blue);letter-spacing:.3px}
.body-copy{font-size:7.6px;line-height:1.55;color:var(--grey)}
.photo{position:absolute}

/* outer left panel */
.feature{position:absolute;left:22px;width:220px}
.feature .icon{width:30px;height:30px;border-radius:50%;background:var(--blue);display:flex;align-items:center;justify-content:center;position:absolute;left:0;top:0}
.feature .heading{font-size:9px;margin-left:40px;line-height:30px}
.feature .body-copy{margin-top:8px}
.divider{position:absolute;left:22px;width:218px;height:1px;background:var(--line)}

/* outer middle */
.market{position:absolute;left:18px;top:14px;width:226px;text-align:center}
.market .heading{font-size:8.5px;margin-bottom:6px;color:var(--charcoal)}

/* brand name placeholder */
.brand{position:absolute;left:0;top:40px;width:262px;display:flex;align-items:center;justify-content:center;gap:8px}
.brand .dot{width:12px;height:12px;border-radius:50%;background:var(--charcoal);flex:none}
.brand-name{font-family:"Open Sans",Arial,sans-serif;font-weight:700;font-size:20px;color:var(--charcoal);white-space:nowrap}

/* outer right */
.name-band{position:absolute;left:0;top:350px;width:262px;height:48px;background:var(--charcoal);padding:9px 0 0 56px}
.name-band .name{font-family:Montserrat,Arial,sans-serif;font-weight:700;font-size:13px;color:#fff;letter-spacing:1px;text-transform:uppercase}
.name-band .title{font-size:7.5px;color:#cfd2d5;margin-top:2px}
.socials{position:absolute;left:14px;top:250px;display:flex;flex-direction:column;gap:8px}
.socials span{width:24px;height:24px;border-radius:50%;background:var(--blue);border:2px solid #fff;display:block}
.contacts{position:absolute;left:56px;top:414px;width:200px}
.contacts li{list-style:none;display:flex;align-items:center;gap:8px;font-size:8.5px;color:var(--charcoal);margin-bottom:9px}
.contacts svg{flex:none}
.web-bar{position:absolute;left:0;bottom:0;height:48px;background:var(--light);display:flex;align-items:center;justify-content:center;font-family:Montserrat,Arial,sans-serif;font-weight:700;font-size:14px;color:var(--blue)}

/* inner left */
.inner .p1{background:var(--light)}
.portrait{position:absolute;left:18px;top:30px;width:76px;height:76px;border-radius:50%;background:radial-gradient(circle at 50% 40%,#b5b2ad,#6f6a66);border:3px solid #fff}
.intro{position:absolute;left:104px;top:26px;width:142px}
.intro-more{position:absolute;left:18px;top:112px;width:226px}
.inner .brand{top:310px}
.blue-band{position:absolute;left:0;bottom:0;width:262px;height:130px;background:var(--blue);padding:14px 18px}
.blue-band .body-copy{color:#e5ecf4}

/* testimonials */
.testi-head{position:absolute;left:282px;top:18px;width:486px;font-size:10px;text-align:center;color:var(--charcoal)}
.quote{position:absolute;border:1px solid var(--line);background:#fff;padding:14px 12px 10px 12px}
.quote .mark-q{position:absolute;left:8px;top:-2px;font-family:Georgia,serif;font-size:28px;color:var(--blue);line-height:1}
.quote .body-copy{padding-top:6px}
.quote .who{font-weight:700;font-size:8px;color:var(--charcoal);text-align:right;margin-top:4px;font-style:italic}
.inner-web{position:absolute;left:262px;top:272px;width:524px;height:28px;border-top:1px solid var(--line);border-bottom:1px solid var(--line);display:flex;align-items:center;justify-content:flex-end;padding-right:24px;font-family:Montserrat,Arial,sans-serif;font-weight:700;font-size:13px;color:var(--blue)}
.stage{position:absolute;width:252px;height:134px}
.stage .tag{position:absolute;left:0;top:0;width:20px;height:100%;background:var(--charcoal);color:#fff;font-family:Montserrat,Arial,sans-serif;font-weight:700;font-size:8px;letter-spacing:2px;writing-mode:vertical-rl;transform:rotate(180deg);display:flex;align-items:center;justify-content:center;text-transform:uppercase}
.stage .photo{left:20px;top:0;width:232px;height:134px}
</style>
</head>
<body>

<section class="spread outer">
  <div class="panel p1">
    <div class="feature" style="top:26px">
      <div class="icon"><svg width="16" height="16" viewBox="0 0 16 16"><path d="M2 12l4-4 3 3 5-6" stroke="#fff" stroke-width="1.8" fill="none"/></svg></div>
      <div class="heading">Adapting the New Trends</div>
      <p class="body-copy">Selling Real Estate has changed dramatically in the last few years. Today, real estate processes are multi-faceted undertakings that encompass significant emotional and financial components.</p>
    </div>
    <div class="divider" style="top:150px"></div>
    <div class="feature" style="top:168px">
      <div class="icon"><svg width="16" height="16" viewBox="0 0 16 16"><circle cx="5" cy="8" r="3" stroke="#fff" stroke-width="1.6" fill="none"/><circle cx="11" cy="8" r="3" stroke="#fff" stroke-width="1.6" fill="none"/></svg></div>
      <div class="heading">Reliable Partnership</div>
      <p class="body-copy">Having the right marketing partner is so important: one who seeks to protect your best interests while capably navigating you through the many complexities of the real estate transaction is vital.</p>
    </div>
    <div class="divider" style="top:292px"></div>
    <div class="feature" style="top:310px">
      <div class="icon"><svg width="16" height="16" viewBox="0 0 16 16"><circle cx="8" cy="8" r="6" stroke="#fff" stroke-width="1.5" fill="none"/><circle cx="8" cy="8" r="2.2" fill="#fff"/></svg></div>
      <div class="heading">Targeting the Right Buyers</div>
      <p class="body-copy">Marta Venholt uses Precision Marketing, specialized tools and technology not only the target precisely, reached through smart targeted channels and proven tools to "showcase" a property to sell targeted to the proper consumer demographic.</p>
    </div>
    <div class="divider" style="top:448px"></div>
    <div class="feature" style="top:466px">
      <div class="icon"><svg width="16" height="16" viewBox="0 0 16 16"><path d="M3 8.5l3.2 3L13 4.5" stroke="#fff" stroke-width="2" fill="none"/></svg></div>
      <div class="heading">Happy Sellers Guaranteed</div>
      <p class="body-copy">A home is one of your most valuable assets. If you are thinking about selling a property, it is crucial that you hire someone with an extraordinary history of happy sellers.</p>
    </div>
  </div>

  <div class="panel p2">
    <div class="market">
      <div class="heading">Proven Market Knowledge</div>
      <p class="body-copy">"That's what you can expect when you work with seasoned specialist Marta Venholt for all your Real Estate needs. The role of a home is an investment, marketing it wisely and with a plan pays off. Select a dedicated, service-minded and results driven broker who understands the intricacies of the Real Estate process... select Marta."</p>
    </div>
    <div class="photo" role="img" aria-label="Photo of a staged kitchen with white cabinets and island" style="left:0;top:150px;width:262px;height:450px;background:linear-gradient(170deg,#d9d3c8 0%,#a99d8c 45%,#6d6154 100%)"></div>
  </div>

  <div class="panel p3">
    <div class="brand"><span class="dot"></span><span class="brand-name">BRAVE Realty LLC</span></div>
    <div class="photo" role="img" aria-label="Photo of a bright open-plan kitchen and dining room" style="left:0;top:115px;width:262px;height:235px;background:linear-gradient(160deg,#e2ddd4 0%,#b9ad9b 50%,#7d7163 100%)"></div>
    <div class="socials"><span></span><span></span><span></span></div>
    <div class="name-band">
      <div class="name">Marta Venholt</div>
      <div class="title">Owner Broker, Stager Re-Designer</div>
    </div>
    <ul class="contacts">
      <li><svg width="12" height="12" viewBox="0 0 12 12"><rect x="1" y="2.5" width="10" height="7" fill="none" stroke="#1f5287" stroke-width="1.2"/><path d="M1 3l5 4 5-4" fill="none" stroke="#1f5287" stroke-width="1.2"/></svg>Marta@LOMAVERTPA.com</li>
      <li><svg width="12" height="12" viewBox="0 0 12 12"><circle cx="6" cy="6" r="5" fill="none" stroke="#1f5287" stroke-width="1.2"/><path d="M1 6h10M6 1c2 2.5 2 7.5 0 10M6 1c-2 2.5-2 7.5 0 10" fill="none" stroke="#1f5287" stroke-width="1"/></svg>LOMAVERTPA.com</li>
      <li><svg width="12" height="12" viewBox="0 0 12 12"><path d="M3 1l2 2.5-1.2 1.5c.8 1.6 1.6 2.4 3.2 3.2L8.5 7 11 9l-1.5 2C5 11 1 7 1 2.5z" fill="#1f5287"/></svg>860-912-7048</li>
    </ul>
    <div class="web-bar" style="width:262px">www.lomavertpa.com</div>
  </div>
</section>

<section class="spread inner">
  <div class="panel p1">
    <div class="portrait" role="img" aria-label="Portrait photo of Marta Venholt"></div>
    <p class="body-copy intro">A veteran in the real estate industry with nearly six years expertise and consistent membership in the Multi Million Dollar Club, combined with her staff, Marta Venholt and BRAVE Realty LLC have extensive</p>
    <p class="body-copy intro-more">expertise in all aspects of the industry. She uses that she takes the advantage of each property, extensively experienced approach to creating beautiful spaces. Marta has a connection with the right buyer and achieves the highest and best offer.</p>
    <div class="brand"><span class="dot"></span><span class="brand-name">BRAVE Realty LLC</span></div>
    <div class="blue-band">
      <p class="body-copy">Marta devotes her efforts to adding real estate by keeping up with the evolving market, researching buyer trends and preparing homes before they enter the market by staging them to connect with the target buyer. With homes all sales are not alike. Therefore, taking a cookie-cutter approach is not acceptable; she recognizes that every property is unique and requires a personalized marketing plan and strategy.</p>
    </div>
  </div>

  <div class="heading testi-head">This is what Marta's clients say about their experiences:</div>

  <div class="quote" style="left:282px;top:44px;width:232px;height:104px">
    <span class="mark-q">“</span>
    <p class="body-copy">In the Real Estate Business there are many, but none like Marta. She brings a level of professionalism far above other Brokers. She will have our house sold fast, with a buyer who loved every detail. Honest, dedicated and a pleasure to work with on every aspect.</p>
    <div class="who">Renata F.</div>
  </div>
  <div class="quote" style="left:282px;top:156px;width:232px;height:110px">
    <span class="mark-q">“</span>
    <p class="body-copy">Marta and her team at BRAVE are knowledgeable and professional. I have been involved in three separate real estate transactions with Marta as a broker and always pleased and impressed by her negotiating skills, her marketing expertise and her ability to manage the process.</p>
    <div class="who">Kelly M.</div>
  </div>
  <div class="quote" style="left:526px;top:44px;width:242px;height:222px">
    <span class="mark-q">“</span>
    <p class="body-copy">Marta directed us right from the beginning by preparing a market comparison using current data, helping us to establish a proper list price. She prepared our property for the market by staging it and then marketed it with great photography and video tours. Because of her eye-catching preparations we received several offers on our house after only a few days. Hearing our interests first, Marta negotiated the best deal for us; we were truly impressed by her knowledge and effort, thank you!</p>
    <div class="who">Jon &amp; Kira P.</div>
  </div>

  <div class="inner-web">www.lomavertpa.com</div>

  <div class="stage" style="left:266px;top:308px"><div class="tag">Before</div><div class="photo" role="img" aria-label="Before photo of an unstaged living room" style="background:linear-gradient(160deg,#cfc6b8,#8d8071)"></div></div>
  <div class="stage" style="left:266px;top:450px"><div class="tag">After</div><div class="photo" role="img" aria-label="After photo of the same living room staged" style="background:linear-gradient(160deg,#e4ddd0,#9c8d7a)"></div></div>
  <div class="stage" style="left:528px;top:308px"><div class="tag">Before</div><div class="photo" role="img" aria-label="Before photo of an unstaged bedroom" style="background:linear-gradient(160deg,#c8c2b9,#7f766c)"></div></div>
  <div class="stage" style="left:528px;top:450px"><div class="tag">After</div><div class="photo" role="img" aria-label="After photo of the same bedroom staged" style="background:linear-gradient(160deg,#e6e1d9,#a39481)"></div></div>
</section>

</body>
</html>
```